velmorino.eu :: Design ideas (no coding) for key pages of Personalized greeting cards online store

We need your vision on modern, clean, easy to read user interface (UI) for online service of personalized printed products, like greeting cards, postcards, fridge magnets, clips and etc.
Your vision should include UI presentation for:
- Home page with login (including soc nets)
- Product Designer page
- Cart pages (products and address selection)
- Example of general internal page (pricing, terms, etc)
- Artist info and portfolio page
We are looking for ideas we will love, NOT complete design of a whole site.
Top design/vision will we used as a basement for separate contract on complete design of the site.

UI should be based on existing functionality with some extent. It should not break ideas or methods used on prototype but designers are free to offer own product presentations, designer’s layout and cart views.

Prototype:
English: http://velmorino.eu
Russian: http://velmorino.ru
Lithuanian: http://velmorino.lt

Target Market(s)

People of 16-45 y.o. who likes to be distinctive, personal.

Industry/Entity Type

Store

Requirements
Must have
• Your work should meet attached requirements.
Site is multilingual. Wording should assume varieties in length on different languages.
Clean and easy to read UI
Flat design preferrably
Should be based on assets which are free or available for royalty-free licensing
Should not have
• heavy, meaningless 3D and shadow effects
Show NOT copy sites like: plonkra.com, tarnwick.co.uk

```html
<!DOCTYPE html>
<html lang="en">
<head>
<meta charset="utf-8">
<title>velmorino – personalized greeting cards</title>
<link href="https://fonts.googleapis.com/css2?family=Open+Sans:wght@400;600&display=swap" rel="stylesheet">
<style>
:root{
  --cream:#fdf2e8;
  --white:#ffffff;
  --red:#d9565a;
  --red-dark:#b73a34;
  --red-text:#d84e4a;
  --navy:#2a4a6b;
  --teal:#2a8a92;
  --grey-text:#333333;
  --grey-mid:#666666;
  --line:#dddddd;
  --panel:#f2f2f2;
  --footer:#fbc98e;
}
*{box-sizing:border-box;margin:0;padding:0}
html,body{width:955px;height:1200px;overflow:hidden;background:var(--white)}
body{font-family:"Open Sans",Arial,sans-serif;color:var(--grey-text);position:relative}
a{text-decoration:none;color:inherit}

.site-header{position:absolute;left:0;top:0;width:955px;height:109px;background:var(--cream)}
.brand{position:absolute;left:98px;top:30px;display:flex;flex-direction:column;align-items:center;gap:8px}
.brand-mark{width:42px;height:42px;background:var(--red-dark)}
.brand-name{font-size:18px;font-weight:400;color:var(--red-dark)}

.account-links{position:absolute;left:566px;top:20px;display:flex;align-items:center;gap:6px;font-size:8.5px;font-weight:600;color:var(--teal);letter-spacing:.3px}
.account-links svg{display:block}
.account-links .sep{color:var(--teal);margin:0 2px}
.lang-select{position:absolute;left:770px;top:15px;width:82px;height:22px;border:1px solid #cfcfcf;background:var(--white);display:flex;align-items:center;padding-left:8px;gap:6px;font-size:9px;color:var(--grey-text)}
.lang-flag{width:18px;height:11px;background:#2c3f87;position:relative}
.lang-flag::before{content:"";position:absolute;left:0;right:0;top:4px;height:3px;background:#d33}
.lang-select .caret{position:absolute;right:8px;top:9px;border-left:5px solid transparent;border-right:5px solid transparent;border-top:5px solid #666}

.main-nav{position:absolute;left:446px;top:66px;width:406px;height:29px;background:linear-gradient(#de6367,#d24f53);border-radius:2px;display:flex;align-items:center;justify-content:space-around;padding:0 6px;font-size:10px;font-weight:600;color:var(--white);letter-spacing:.3px}

.hero{position:absolute;left:103px;top:120px;width:749px;height:308px;border:2px solid #e3e3e3;background:var(--panel)}
.category-list{position:absolute;left:-2px;top:-2px;width:193px;list-style:none}
.category-list li{height:34.4px;display:flex;align-items:center;padding-left:14px;font-size:10px;font-weight:600;letter-spacing:.4px;color:var(--red-text);border-bottom:2px solid var(--white);background:var(--panel)}
.category-list li::before{content:"";width:4px;height:4px;border-right:1.6px solid var(--navy);border-top:1.6px solid var(--navy);transform:rotate(45deg);margin-right:11px}
.category-list li.active{color:var(--navy);background:var(--white);border:2px solid #e3e3e3;font-size:11.5px;height:32px}
.hero-stage{position:absolute;left:192px;top:0;right:0;bottom:0;background:#f4f4f4;border-left:2px solid #e3e3e3}
.hero-art{position:absolute;left:12px;top:20px;width:335px;height:276px;background:linear-gradient(135deg,#e9c9c0 0%,#efe6d6 45%,#f3dcc4 70%,#8a8a8a 100%);border-radius:4px;opacity:.9}
.hero-copy{position:absolute;right:22px;top:62px;width:260px;text-align:right}
.hero-copy h1{font-size:21px;font-weight:400;line-height:24px;color:var(--red-dark)}
.hero-copy p{margin-top:8px;font-size:11px;line-height:17px;color:var(--grey-text)}
.hero-dots{position:absolute;left:480px;top:278px;display:flex;gap:3px}
.hero-dots span{width:10px;height:10px;border-radius:50%;background:#8a8a8a}
.hero-dots span.on{background:var(--teal)}

.featured{position:absolute;left:0;top:450px;width:955px;height:327px;background:var(--cream)}
.featured h2{position:absolute;left:103px;top:22px;font-size:16px;font-weight:400;letter-spacing:.5px;color:var(--red-dark)}
.view-tools{position:absolute;left:488px;top:19px;display:flex;align-items:center;gap:10px}
.view-tools .divider{width:1px;height:24px;background:#e7a3a1}
.filter{position:absolute;top:17px;height:27px;width:82px;border:1px solid #d9d9d9;background:var(--white);display:flex;align-items:center;padding-left:8px;gap:8px;font-size:9.5px;color:var(--grey-text)}
.filter .swatch{width:13px;height:13px;background:var(--red)}
.filter .caret{position:absolute;right:8px;top:11px;border-left:5px solid transparent;border-right:5px solid transparent;border-top:5px solid #666}
.filter-color{left:682px}
.filter-occasion{left:770px}

.product-grid{position:absolute;left:103px;top:57px;display:flex;gap:16px}
.product-card{width:176px;height:255px;background:var(--white);border:1px solid #e2d7cc;position:relative}
.product-image{position:absolute;left:6px;top:6px;width:162px;height:117px}
.product-card h3{position:absolute;left:7px;top:131px;width:160px;font-size:11.5px;font-weight:400;line-height:16px;color:var(--red-text)}
.product-card p{position:absolute;left:7px;top:164px;width:160px;font-size:10.5px;line-height:14.5px;color:var(--grey-text)}
.price{position:absolute;left:7px;top:213px;font-size:17px;color:var(--teal)}
.card-actions{position:absolute;right:10px;top:218px;display:flex;align-items:center;gap:14px}
.card-actions .add{width:14px;height:14px;background:var(--red)}
.color-strip{position:absolute;left:0;right:0;bottom:0;height:5px;background:linear-gradient(90deg,#bbb 0 6%,#f0a 6% 10%,#ccc 10% 14%,#9a6 14% 18%,#c3a 18% 22%,#555 22% 28%,#4a4 28% 33%,#eee 33% 37%,#e93 37% 42%,#222 42% 46%,#d44 46% 50%,#3cf 50% 55%,#fc3 55% 59%,#36c 59% 64%,#f66 64% 68%,#8c5 68% 73%,#17c 73% 78%,#fa0 78% 82%,#c22 82% 87%,#6c3 87% 92%,#39c 92% 96%,#6a2 96% 100%)}

.videos{position:absolute;left:0;top:777px;width:955px;height:327px;background:var(--white)}
.section-title{position:absolute;left:103px;top:16px;width:749px;display:flex;align-items:center;gap:28px;font-size:18px;font-weight:400;letter-spacing:1px;color:#555}
.section-title::before,.section-title::after{content:"";flex:1;height:1px;background:#e08a86}
.video-frame{position:absolute;left:230px;top:53px;width:495px;height:257px;border:1px solid #dcdcdc;padding:3px;background:var(--white)}
.video-still{width:100%;height:100%;background:radial-gradient(ellipse at 55% 55%,#e8d6dc 0 22%,#6a4a4a 34%,#34463a 48%,#263a2c 100%)}
.play{position:absolute;left:222px;top:95px}
.slider-arrow{position:absolute;top:163px}
.slider-prev{left:175px}
.slider-next{left:762px}

.site-footer{position:absolute;left:0;top:1104px;width:955px;height:96px;background:var(--footer)}
.footer-links{position:absolute;left:105px;top:20px;font-size:11px;color:var(--grey-text)}
.footer-links .slash{margin:0 5px}
.copyright{position:absolute;left:105px;top:56px;font-size:10px;color:var(--red-dark)}
.copyright b{font-weight:400;color:var(--grey-text)}
.follow{position:absolute;left:660px;top:12px;font-size:11.5px;font-weight:600;letter-spacing:.5px;color:var(--grey-text)}
.social{position:absolute;left:662px;top:43px;display:flex;gap:7px}
.social span{width:33px;height:33px;border-radius:50%;display:block}
</style>
</head>
<body>

<header class="site-header">
  <a class="brand" href="#">
    <span class="brand-mark"></span>
    <span class="brand-name">velmorino</span>
  </a>
  <nav class="account-links">
    <svg width="9" height="11" viewBox="0 0 9 11"><rect x="0" y="4.5" width="9" height="6.5" fill="#444"/><path d="M2 4.5V3a2.5 2.5 0 0 1 5 0v1.5" fill="none" stroke="#444" stroke-width="1.4"/></svg>
    <a href="#">LOG IN</a><span class="sep">|</span>
    <svg width="11" height="11" viewBox="0 0 11 11"><circle cx="5.5" cy="3" r="2.6" fill="#444"/><path d="M0.5 11a5 4.5 0 0 1 10 0z" fill="#444"/></svg>
    <a href="#">SIGN IN</a><span class="sep">|</span>
    <svg width="13" height="11" viewBox="0 0 13 11"><path d="M0 1h2.5l1.8 6h6.5l1.5-4.5H3.5" fill="none" stroke="#444" stroke-width="1.2"/><circle cx="5" cy="9.5" r="1.1" fill="#444"/><circle cx="10" cy="9.5" r="1.1" fill="#444"/></svg>
    <a href="#">MY CART</a>
  </nav>
  <div class="lang-select"><span class="lang-flag"></span>Eng<span class="caret"></span></div>
  <nav class="main-nav">
    <a href="#">HOME</a><a href="#">ABOUT US</a><a href="#">PRODUCTS</a><a href="#">CATEGORIES</a><a href="#">AUTHORS</a>
  </nav>
</header>

<section class="hero">
  <ul class="category-list">
    <li class="active">GREETING CARDS</li>
    <li>POST CARDS</li>
    <li>FRIDGE MAGNETS</li>
    <li>WOODEN BOARDS WITH CLIP</li>
    <li>T-SHIRTS</li>
    <li>CUPS</li>
    <li>MUGS</li>
    <li>HEAD CUPS</li>
    <li>AND MORE</li>
  </ul>
  <div class="hero-stage">
    <div class="hero-art" role="img" aria-label="Fan of illustrated greeting cards with winter and festive motifs"></div>
    <div class="hero-copy">
      <h1>The individual greeting cards according to your mood</h1>
      <p>Aliquam molestie, mi et imperdiet euismod, dui purus auctor tellus, et interdum lacus lectus et ante.</p>
    </div>
    <div class="hero-dots"><span class="on"></span><span></span><span></span><span></span></div>
  </div>
</section>

<section class="featured">
  <h2>FEATURED PRODUCTS</h2>
  <div class="view-tools">
    <svg width="20" height="20" viewBox="0 0 20 20"><g stroke="#b73a34" stroke-width="2.6" stroke-linecap="round"><path d="M10 1v18M2.2 5.5l15.6 9M2.2 14.5l15.6-9"/></g></svg>
    <span class="divider"></span>
    <svg width="40" height="22" viewBox="0 0 40 22"><g fill="none" stroke="#444" stroke-width="1"><rect x="1" y="6" width="15" height="15"/><path d="M1 6l5-5h10"/><rect x="16" y="11" width="22" height="10"/><path d="M16 11l3-3h19l-2 3"/></g></svg>
    <span class="divider"></span>
    <svg width="20" height="22" viewBox="0 0 20 22"><g fill="none" stroke="#444" stroke-width="1"><rect x="1" y="6" width="16" height="15"/><path d="M1 6l5-5h11v5"/></g></svg>
    <span class="divider"></span>
    <svg width="40" height="22" viewBox="0 0 40 22"><g fill="none" stroke="#444" stroke-width="1"><rect x="1" y="3" width="14" height="18"/><rect x="17" y="9" width="21" height="12"/></g></svg>
  </div>
  <div class="filter filter-color">Color<span class="swatch"></span><span class="caret"></span></div>
  <div class="filter filter-occasion">Birthday<span class="caret"></span></div>

  <div class="product-grid">
    <article class="product-card">
      <div class="product-image" role="img" aria-label="Patchwork card illustration with a toy bear" style="background:linear-gradient(135deg,#e8e4d6,#b9c9e0 55%,#f0efe6)"></div>
      <h3>Duis aliquam nibh a dui iaculis...</h3>
      <p>Aenean a nibh eget turpis vehicula tempus ac sed massa.</p>
      <span class="price">€ 2.99</span>
      <div class="card-actions"><svg width="10" height="13" viewBox="0 0 10 13"><path d="M3 1v8.5" stroke="#444" stroke-width="1.6"/><ellipse cx="2.8" cy="10.5" rx="2.6" ry="2" fill="#444"/><path d="M3 1q5 1 6 5" fill="none" stroke="#444" stroke-width="1.6"/></svg><span class="add"></span></div>
      <span class="color-strip"></span>
    </article>
    <article class="product-card">
      <div class="product-image" role="img" aria-label="Birthday card illustration with a large number eighteen and gifts" style="background:linear-gradient(135deg,#fbe9d4,#f6a270 50%,#fbe4c8)"></div>
      <h3>Duis aliquam nibh a dui iaculis...</h3>
      <p>Aenean a nibh eget turpis vehicula tempus ac sed massa.</p>
      <span class="price">€ 2.99</span>
      <div class="card-actions"><svg width="10" height="13" viewBox="0 0 10 13"><path d="M3 1v8.5" stroke="#444" stroke-width="1.6"/><ellipse cx="2.8" cy="10.5" rx="2.6" ry="2" fill="#444"/><path d="M3 1q5 1 6 5" fill="none" stroke="#444" stroke-width="1.6"/></svg><span class="add"></span></div>
      <span class="color-strip"></span>
    </article>
    <article class="product-card">
      <div class="product-image" role="img" aria-label="Festive card with white flowers and pine cones on red" style="background:radial-gradient(circle at 50% 50%,#e9e4d2 0 25%,#4f7a3a 45%,#b82422 75%)"></div>
      <h3>Duis aliquam nibh a dui iaculis...</h3>
      <p>Aenean a nibh eget turpis vehicula tempus ac sed massa.</p>
      <span class="price">€ 2.99</span>
      <div class="card-actions"><svg width="10" height="13" viewBox="0 0 10 13"><path d="M3 1v8.5" stroke="#444" stroke-width="1.6"/><ellipse cx="2.8" cy="10.5" rx="2.6" ry="2" fill="#444"/><path d="M3 1q5 1 6 5" fill="none" stroke="#444" stroke-width="1.6"/></svg><span class="add"></span></div>
      <span class="color-strip"></span>
    </article>
    <article class="product-card">
      <div class="product-image" role="img" aria-label="Sunny card illustration with a child in a striped cap and flowers" style="background:linear-gradient(160deg,#f7c23a 0 25%,#d6eef8 45%,#e9f4fb 80%)"></div>
      <h3>Duis aliquam nibh a dui iaculis...</h3>
      <p>Aenean a nibh eget turpis vehicula tempus ac sed massa.</p>
      <span class="price">€ 2.99</span>
      <div class="card-actions"><svg width="10" height="13" viewBox="0 0 10 13"><path d="M3 1v8.5" stroke="#444" stroke-width="1.6"/><ellipse cx="2.8" cy="10.5" rx="2.6" ry="2" fill="#444"/><path d="M3 1q5 1 6 5" fill="none" stroke="#444" stroke-width="1.6"/></svg><span class="add"></span></div>
      <span class="color-strip"></span>
    </article>
  </div>
</section>

<section class="videos">
  <h2 class="section-title">VIDEOS</h2>
  <div class="video-frame">
    <div class="video-still" role="img" aria-label="Video still of a handmade card with a pink paper flower on a dark green table"></div>
    <svg class="play" width="50" height="50" viewBox="0 0 50 50"><circle cx="25" cy="25" r="24" fill="#ffffff" opacity=".85"/><path d="M19 14l16 11-16 11z" fill="#555"/></svg>
  </div>
  <svg class="slider-arrow slider-prev" width="16" height="28" viewBox="0 0 16 28"><path d="M14 2L3 14l11 12" fill="none" stroke="#999" stroke-width="2"/></svg>
  <svg class="slider-arrow slider-next" width="16" height="28" viewBox="0 0 16 28"><path d="M2 2l11 12L2 26" fill="none" stroke="#999" stroke-width="2"/></svg>
</section>

<footer class="site-footer">
  <nav class="footer-links">
    <a href="#">About us</a><span class="slash">/</span><a href="#">How it works</a><span class="slash">/</span><a href="#">Prices</a><span class="slash">/</span><a href="#">Rules</a><span class="slash">/</span><a href="#">Contacts</a>
  </nav>
  <p class="copyright">Copyright © 2014 <b>velmorino.</b> All Right Reserved</p>
  <p class="follow">FOLLOW US:</p>
  <div class="social" aria-label="Social links">
    <span style="background:#1d3e73"></span>
    <span style="background:#3fb4e8"></span>
    <span style="background:#c8262a"></span>
    <span style="background:#444444"></span>
    <span style="background:#a5674a"></span>
  </div>
</footer>

</body>
</html>
```